Kellwood Build, Carpentry Services

Business card for carpentry business in the Sunshine Coast.

Business card layout required using logo provided - provided both PDF copy and AI. Please let me know if you would like a the files for the logo symbol and text by itself.

Business Colours are grey, blue and white. The font colours codes for this design are Blue Hex # 00B4E6 and Hex # 39393B for the gray colour.

FYI font for logo is Gotham Bold.

Preference for a clean and striking layout that is simple and elegant.

Target Market(s)

Young Families, retirees, young couples requiring assistance with small to medium works/renovations on the Sunshine Coast.

Industry/Entity Type

Construction

Contact Information for Business Card

Dean Kellwood
Carpenter
0489305627
dean@kellwoodbuild.com.au
Pelican Bay, Seabreeze Coast
RHPA Licensed Carpenter (In smaller font)

Font styles to use
Sans Serif

Colors

Designer to choose colors to be used in the design.

Requirements
Must have
• Logo provided must appear on the card, preferably on one side of the card by itself with the text on the alternate side
Nice to have
• Text on the other side of card, maybe grey background and white font here but happy for the designer to provide ideas here.
Should not have
• Use of other colours, other than the ones provided - white, grey and blue. Black optional.

```html
<!DOCTYPE html>
<html lang="en">
<head>
<meta charset="UTF-8">
<title>Kellwood Build – Business Card</title>
<link rel="stylesheet" href="https://fonts.googleapis.com/css2?family=Montserrat:wght@400;500;700&display=swap">
<style>
  :root {
    --brand-blue: #00B4E6;
    --card-grey: #39393B;
    --card-grey-back: #363638;
    --stage: #141414;
    --white: #FFFFFF;
    --soft-white: #E9E9EA;
  }
  * { box-sizing: border-box; margin: 0; padding: 0; }
  html, body {
    width: 1200px;
    height: 900px;
    overflow: hidden;
    background: var(--stage);
    font-family: "Montserrat", sans-serif;
  }
  .canvas {
    position: relative;
    width: 1200px;
    height: 900px;
  }
  .card {
    position: absolute;
    left: 290px;
    width: 620px;
    height: 354px;
    border-radius: 4px;
    box-shadow: 0 18px 40px rgba(0,0,0,0.55);
  }
  .card--back {
    top: 60px;
    background: var(--card-grey-back);
    display: flex;
    align-items: center;
    justify-content: center;
  }
  .card--front {
    top: 476px;
    background: var(--card-grey);
    display: flex;
    align-items: center;
    padding: 0 28px 0 30px;
  }

  /* back side: brand name alone */
  .back-brand {
    display: flex;
    align-items: center;
    gap: 16px;
  }
  .back-brand__square {
    width: 30px;
    height: 30px;
    background: var(--soft-white);
  }
  .back-brand__name {
    color: var(--soft-white);
    font-weight: 700;
    font-size: 34px;
    letter-spacing: 2px;
    text-transform: uppercase;
  }

  /* front side */
  .brand {
    display: flex;
    align-items: center;
    gap: 12px;
    width: 230px;
    flex: 0 0 auto;
  }
  .brand__square {
    width: 22px;
    height: 22px;
    background: var(--brand-blue);
    flex: 0 0 auto;
  }
  .brand__name {
    color: var(--brand-blue);
    font-weight: 700;
    font-size: 22px;
    letter-spacing: 1px;
    text-transform: uppercase;
    line-height: 1.15;
  }
  .divider {
    width: 2px;
    height: 150px;
    background: var(--brand-blue);
    margin: 0 16px 0 10px;
    flex: 0 0 auto;
  }
  .contact {
    color: var(--white);
  }
  .contact__name {
    color: var(--brand-blue);
    font-weight: 700;
    font-size: 22px;
    letter-spacing: 1px;
    text-transform: uppercase;
    line-height: 1.1;
  }
  .contact__role {
    font-size: 15px;
    font-weight: 400;
    margin-top: 2px;
    margin-bottom: 12px;
  }
  .contact__list {
    list-style: none;
  }
  .contact__item {
    display: flex;
    align-items: center;
    gap: 8px;
    font-size: 15px;
    font-weight: 400;
    line-height: 1.5;
    white-space: nowrap;
  }
  .contact__icon {
    width: 14px;
    height: 14px;
    flex: 0 0 auto;
  }
  .contact__licence {
    font-size: 13px;
    font-weight: 400;
    margin-top: 10px;
    color: var(--soft-white);
  }
</style>
</head>
<body>
<main class="canvas">

  <section class="card card--back" aria-label="Card back">
    <div class="back-brand">
      <span class="back-brand__square"></span>
      <span class="back-brand__name">Kellwood Build</span>
    </div>
  </section>

  <section class="card card--front" aria-label="Card front">
    <div class="brand">
      <span class="brand__square"></span>
      <span class="brand__name">Kellwood<br>Build</span>
    </div>

    <span class="divider"></span>

    <div class="contact">
      <h1 class="contact__name">Dean Kellwood</h1>
      <p class="contact__role">Carpenter</p>
      <ul class="contact__list">
        <li class="contact__item">
          <svg class="contact__icon" viewBox="0 0 16 16" aria-hidden="true">
            <circle cx="8" cy="8" r="7" fill="none" stroke="var(--brand-blue)" stroke-width="1.3"/>
            <path d="M5.6 4.6l1.2 1.6-.7.9c.5 1 1.3 1.8 2.3 2.3l.9-.7 1.6 1.2-.6 1.1c-2.7-.3-4.9-2.5-5.2-5.2z" fill="var(--brand-blue)"/>
          </svg>
          <span>0489 305 627</span>
        </li>
        <li class="contact__item">
          <svg class="contact__icon" viewBox="0 0 16 16" aria-hidden="true">
            <rect x="1" y="3" width="14" height="10" fill="none" stroke="var(--brand-blue)" stroke-width="1.3"/>
            <path d="M1 3l7 6 7-6" fill="none" stroke="var(--brand-blue)" stroke-width="1.3"/>
          </svg>
          <span>dean@kellwoodbuild.com.au</span>
        </li>
        <li class="contact__item">
          <svg class="contact__icon" viewBox="0 0 16 16" aria-hidden="true">
            <path d="M8 1.5L1 8h2v6.5h4v-4h2v4h4V8h2z" fill="var(--brand-blue)"/>
          </svg>
          <span>Pelican Bay, Seabreeze Coast</span>
        </li>
      </ul>
      <p class="contact__licence">RHPA Licensed Carpenter</p>
    </div>
  </section>

</main>
</body>
</html>
```